Business card design to suit our website

Need a nice looking business card for our business based off images from our Website and provided images. The business card will require 2 different names (for the 2 owners). The business card should include images from our website, facebook (keel bracket works set) or the pictures provided. it should also contain all contact information.
Our website is www.keelbracketworks.com.au
Please dont use image from top bar of website. If images are used please use the ones of our product under the buy it now tab

Target Market(s)

Automotive

Industry/Entity Type

Automotive Part

Contact Information for Business Card

Business Name. contact details including names phone number email. logo
2 business cards needed with 2 different persons names and phone number.

Colors

Designer to choose colors to be used in the design.

Requirements
Must have
• whatever looks best

```html
<!DOCTYPE html>
<html lang="en">
<head>
<meta charset="utf-8">
<title>Keel Bracket Works Set – Business Card</title>
<link rel="stylesheet" href="https://fonts.googleapis.com/css2?family=Arimo:wght@400;700&family=Open+Sans:wght@400&display=swap">
<style>
  :root {
    --backdrop: #8c8c8c;
    --card-white: #f4f4f4;
    --brand-red: #be1e2d;
    --ink: #1a1a1a;
    --night: #000000;
    --rule: #555555;
    --paper: #ffffff;
  }
  * { box-sizing: border-box; margin: 0; padding: 0; }
  html, body { width: 1200px; height: 1200px; overflow: hidden; }
  body {
    background: var(--backdrop);
    position: relative;
    font-family: "Arimo", Arial, sans-serif;
  }
  .card {
    position: absolute;
    top: 310px;
    height: 594px;
    box-shadow: 2px 3px 5px rgba(0,0,0,0.35);
    overflow: hidden;
  }
  .card-front {
    left: 234px;
    width: 364px;
    background: var(--card-white);
    text-align: center;
    color: var(--ink);
  }
  .brand-name {
    position: absolute;
    top: 140px;
    left: 0;
    width: 100%;
    color: var(--brand-red);
    font-weight: 700;
    font-size: 34px;
    line-height: 40px;
  }
  .person-name {
    position: absolute;
    top: 384px;
    width: 100%;
    color: var(--brand-red);
    font-weight: 700;
    font-size: 22px;
  }
  .person-role {
    position: absolute;
    top: 408px;
    width: 100%;
    font-size: 17px;
  }
  .divider {
    position: absolute;
    top: 449px;
    left: 84px;
    width: 197px;
    border-top: 1px solid var(--rule);
  }
  .contact-list {
    position: absolute;
    top: 468px;
    width: 100%;
    list-style: none;
    font-size: 17px;
    line-height: 21.5px;
  }
  .contact-label { color: var(--brand-red); font-weight: 700; }
  .card-back {
    left: 628px;
    width: 368px;
    background: var(--brand-red);
  }
  .back-art { position: absolute; inset: 0; }
  .back-brand {
    position: absolute;
    top: 370px;
    width: 100%;
    text-align: center;
    color: var(--paper);
    font-weight: 700;
    font-size: 30px;
    line-height: 36px;
  }
  .back-url {
    position: absolute;
    top: 530px;
    width: 100%;
    text-align: center;
    color: var(--paper);
    font-family: "Open Sans", Arial, sans-serif;
    font-size: 17px;
  }
</style>
</head>
<body>
  <section class="card card-front">
    <p class="brand-name">Keel Bracket<br>Works Set</p>
    <p class="person-name">DANIEL HARPER</p>
    <p class="person-role">Managing Director</p>
    <div class="divider"></div>
    <ul class="contact-list">
      <li><span class="contact-label">P:</span> 1300 482 617</li>
      <li><span class="contact-label">M:</span> 0412 586 304</li>
      <li><span class="contact-label">E:</span> sales@keelbracketworks.com.au</li>
      <li><span class="contact-label">W:</span> www.keelbracketworks.com.au</li>
    </ul>
  </section>

  <section class="card card-back">
    <svg class="back-art" width="368" height="594" viewBox="0 0 368 594" aria-hidden="true">
      <path d="M4 0 H368 V310 C320 300 250 260 180 230 C110 200 50 170 26 120 Z" fill="var(--night)"/>
    </svg>
    <p class="back-brand">Keel Bracket<br>Works Set</p>
    <p class="back-url">www.keelbracketworks.com.au</p>
  </section>
</body>
</html>
```